Are Your Bloom Within? Innovative Company Needs a Web Design *Guaranteed*

We need a web design for our coaching company that helps college women overcome depression and anxiety without the stigma or hassle of traditional therapy. Ultimately, we need a website that conveys that we are the world's leading experts in this area. That is our focus. It must invite a very trusting and free spirited feminine atmoshpere that a college girl would cherish and would not hesitate to revist again and again. We need a balance of being the experts and being a laid-back party spot, a place where our college clients become absolute raving fans of our service and take action. It should be easy on the eyes, great to look at, and makes a awesome first impression. We would like to see the color scheme match our logo coloring as well.

Target Market(s)

College Women

Requirements
Must have
• Social media integration is vital. This webpage should also be mobile friendly, a good balance of flash and flow yet simplicity. It must follow the placement format we have provided. Arial, Verdana fonts preferred. Our objective is for them to "see what we are all about" in just a glimpse of the page, without scrolling down or actions, more specifically to draw ALL attention to watch our pitch video.
Nice to have
• Since our logo has a flower on it, Im curious to see what can be done with that coloring. Perhaps a tropic of Hawaiian theme? Plants are metaphoric for growth and are always a nice background. A pop-up upon entering page to capture emails for free content would be really nice to collect their name, cell, email, biggest challenge.
Should not have
• No ugly colors. Nothing that is to serious. And most importantly, we want to convey we are experts. The design cannot give the impression that we are some large, dark, ominous company with a shady agenda. College students do not trust companies like this especially since most are only out for their money. We want to separate ourselves from the pack and prove we are all about them and always on their side.

```html
<!DOCTYPE html>
<html lang="en">
<head>
<meta charset="utf-8">
<title>Bloom Within</title>
<link rel="stylesheet" href="https://fonts.googleapis.com/css2?family=Open+Sans:wght@400;600&family=PT+Sans+Narrow:wght@400;700&family=Ubuntu:wght@400;500;700&display=swap">
<style>
:root{
  --bg:#eeeeee;
  --page:#ffffff;
  --nav:#5b8be0;
  --nav-dark:#4a78cf;
  --blue:#1a7ad0;
  --link:#2a78c8;
  --pink:#e0357f;
  --ink:#2a2a2a;
  --body:#333333;
  --muted:#888888;
  --rule:#ececec;
  --footer:#3b3b3b;
  --footer-rule:#4c4c4c;
  --footer-text:#f2f2f2;
  --footer-muted:#9a9a9a;
  --play:#c4141b;
}
*{margin:0;padding:0;box-sizing:border-box}
html,body{width:1109px;height:1200px;overflow:hidden}
body{background:var(--bg);font-family:Arial,Helvetica,sans-serif;color:var(--body);position:relative}
.page{position:absolute;left:184px;top:0;width:740px;height:1200px;background:var(--page);box-shadow:0 0 3px rgba(0,0,0,.15)}
.abs{position:absolute}

/* header */
.brand{left:30px;top:46px;display:flex;align-items:center;gap:8px;font-family:Ubuntu,sans-serif;font-weight:500;font-size:20px;color:var(--pink)}
.brand-dot{width:14px;height:14px;border-radius:50%;background:var(--pink)}
.socialize{right:3px;top:58px;text-align:right}
.socialize-label{font-size:10px;color:#c8c8c8;margin-bottom:4px}
.social-row{display:flex;gap:3px}
.social-row span{width:14px;height:14px;border-radius:3px}

/* nav */
.ribbon{top:133px}
.ribbon-left{left:-41px}
.ribbon-right{right:-41px}
.nav{left:0;top:111px;width:740px;height:44px;background:var(--nav);display:flex;align-items:center;padding-left:28px}
.nav a{color:#fff;text-decoration:none;font-size:11px;margin-right:29px;text-shadow:0 1px 0 rgba(0,0,0,.2)}
.search{position:absolute;left:594px;top:12px;width:111px;height:18px;background:#b9cdf2}
.search-icon{position:absolute;left:716px;top:13px}

/* quote */
.quote{left:0;top:174px;width:740px;text-align:center;font-family:Ubuntu,sans-serif;font-size:23px;line-height:23px;color:var(--ink)}
.rule{left:0;width:740px;height:1px;background:var(--rule)}

/* hero */
.hero-title{left:25px;top:257px;font-family:Ubuntu,sans-serif;font-weight:500;font-size:25px;line-height:27.5px;color:var(--ink)}
.hero-title b{color:var(--blue);font-weight:700}
.hero-copy{left:25px;top:387px;width:240px;font-size:8.6px;line-height:12.6px;color:var(--body)}
.cta{left:25px;top:455px;width:213px;height:30px;border-radius:4px;background:linear-gradient(#3e95e6,#1766c4);color:#fff;font-family:"PT Sans Narrow",sans-serif;font-size:17px;letter-spacing:.5px;display:flex;align-items:center;justify-content:center;box-shadow:0 2px 2px rgba(0,0,0,.25)}
.video{left:292px;top:254px;width:414px;height:280px;box-shadow:0 2px 8px rgba(0,0,0,.3);background:#e0e0e0}
.video-still{width:414px;height:255px;background:linear-gradient(100deg,#d9c6b4 0%,#efe6dc 35%,#e4e0d8 55%,#8a7a3a 75%,#a89070 100%)}
.play-big{position:absolute;left:167px;top:81px}
.controls{position:absolute;left:0;top:255px;width:414px;height:25px;background:linear-gradient(#f2f2f2,#d8d8d8);display:flex;align-items:center;font-size:7px;color:#555}
.track{position:absolute;left:38px;top:10px;width:206px;height:5px;border-radius:3px;background:#555}
.track-fill{width:100px;height:5px;border-radius:3px;background:var(--play)}
.knob{position:absolute;left:95px;top:-3px;width:10px;height:10px;border-radius:50%;background:#eee;border:1px solid #999}
.time{position:absolute;left:251px;top:9px}
.vol{position:absolute;left:324px;top:10px;width:52px;height:5px;border-radius:3px;background:#555}

/* benefits */
.section-title{font-family:"Open Sans",sans-serif;font-size:12.5px;color:#444;letter-spacing:-.6px;text-transform:uppercase}
.benefits-title{left:0;top:598px;width:740px;text-align:center}
.benefits-underline{left:316px;top:616px;width:100px;height:1px;background:#bbb}
.carousel{left:19px;top:626px;width:702px;height:118px;border-radius:8px;background:linear-gradient(#f1f1f1,#e6e6e6);border:1px solid #e0e0e0}
.arrow-btn{position:absolute;top:41px;width:23px;height:23px;border-radius:50%;background:#fff;box-shadow:0 1px 2px rgba(0,0,0,.2);display:flex;align-items:center;justify-content:center}
.thumb{position:absolute;top:7px;width:120px;height:104px;background:#fff;padding:3px;box-shadow:0 0 2px rgba(0,0,0,.2)}
.thumb div{width:100%;height:100%}

/* features & testimonial */
.features-title{left:21px;top:797px}
.features-copy{left:21px;top:819px;width:300px;font-size:8.6px;line-height:12.6px}
.features-copy a{color:var(--link);text-decoration:none}
.students-title{left:341px;top:797px}
.testimonial{left:342px;top:828px;width:366px;height:138px;background:#fff;box-shadow:0 1px 4px rgba(0,0,0,.12)}
.avatar{position:absolute;left:18px;top:16px;width:40px;height:40px;border-radius:50%;background:radial-gradient(#5c7070,#23302f)}
.t-title{position:absolute;left:82px;top:23px;font-family:"Open Sans",sans-serif;font-size:10px;color:var(--link)}
.t-meta{position:absolute;left:83px;top:38px;font-size:8px;color:#aaa}
.t-meta b{color:#777}
.t-body{position:absolute;left:83px;top:58px;width:270px;font-size:8.3px;line-height:12.6px;color:#666}
.t-more{position:absolute;left:83px;top:108px;font-size:8.3px;color:var(--link)}
.t-arrow{position:absolute;left:268px;top:103px;color:#e06a4a;font-size:12px}

/* footer */
.footer-line{left:0;top:998px;width:740px;height:5px;background:var(--pink)}
.footer{left:0;top:1003px;width:740px;height:197px;background:var(--footer);color:var(--footer-text)}
.f-head{position:absolute;top:17px;font-size:11px;font-weight:bold}
.quick{position:absolute;left:20px;top:45px;width:171px;list-style:none}
.quick li{font-size:8.8px;height:21px;line-height:14px;border-bottom:1px solid var(--footer-rule);padding-top:2px}
.quick li:last-child{border-bottom:none}
.stay-sub{position:absolute;left:242px;top:37px;font-size:8.8px;color:var(--footer-muted)}
.stay-list{position:absolute;left:240px;top:60px;list-style:none}
.stay-list li{display:flex;align-items:center;gap:10px;font-size:8.8px;color:#ccc;height:21.5px}
.stay-list span{width:16px;height:16px;border-radius:3px}
.contact{position:absolute;right:31px;top:17px;text-align:right;font-size:8.8px;line-height:13px}
.contact .muted{color:var(--footer-muted)}
.back-top{position:absolute;right:30px;top:150px;display:flex;align-items:center;gap:6px;font-size:8.8px;color:var(--footer-muted)}
.back-top span{width:14px;height:14px;border-radius:50%;background:var(--pink)}
</style>
</head>
<body>
<div class="page">

  <header>
    <div class="abs brand"><span class="brand-dot"></span>Bloom Within</div>
    <div class="abs socialize">
      <div class="socialize-label">Socialize</div>
      <div class="social-row">
        <span style="background:#3ab5ea"></span><span style="background:#c9302c"></span><span style="background:#3b5a9a"></span><span style="background:#f4f4f4;border:1px solid #ddd"></span><span style="background:#dc4a38"></span><span style="background:#f29a1f"></span>
      </div>
    </div>
  </header>

  <svg class="abs ribbon ribbon-left" width="41" height="44" viewBox="0 0 41 44"><path d="M0 -22 H41 V22 H0 L14 0 Z" transform="translate(0,22)" fill="var(--nav-dark)"/></svg>
  <svg class="abs ribbon ribbon-right" width="41" height="44" viewBox="0 0 41 44"><path d="M41 0 H0 V44 H41 L27 22 Z" fill="var(--nav-dark)"/></svg>
  <nav class="abs nav">
    <a href="#">HOME</a><a href="#">PRODUCT</a><a href="#">PARENTS</a><a href="#">HOW IT WORKS</a><a href="#">ABOUT US</a><a href="#">CONTACT US</a>
    <div class="search"></div>
    <svg class="search-icon" width="14" height="16" viewBox="0 0 14 16"><circle cx="8" cy="6" r="4" fill="none" stroke="#fff" stroke-width="2"/><line x1="5" y1="9" x2="1" y2="14" stroke="#fff" stroke-width="2.4" stroke-linecap="round"/></svg>
  </nav>

  <p class="abs quote">‘Lorem ipsum dolor sit amet, consectetur adipisicing elit,<br>sed do eiusmod tempor incididunt ut labore et’</p>
  <div class="abs rule" style="top:234px"></div>

  <h1 class="abs hero-title">How college women<br>kick <b>DEPRESSION</b><br>and <b>ANXIETY</b>...<br>for Good</h1>
  <p class="abs hero-copy">Duis aute irure dolor in reprehenderit in voluptate velit esse cillum dolore eu fugiat nulla pariatur. Excepteur sint occaecat cupidatat non proident, sunt in culpa qui officia deserunt mollit anim id est laborum.</p>
  <div class="abs cta">CLICK TO KNOW HOW</div>

  <div class="abs video">
    <div class="video-still" role="img" aria-label="Video still: two young women talking on a bed in a bright room"></div>
    <svg class="play-big" width="80" height="80" viewBox="0 0 80 80"><circle cx="40" cy="40" r="38" fill="var(--play)" stroke="#8c0c10" stroke-width="2"/><path d="M30 22 L60 40 L30 58 Z" fill="#fff"/></svg>
    <div class="controls">
      <svg class="abs" style="left:11px;top:7px" width="12" height="12" viewBox="0 0 12 12"><path d="M1 0 L11 6 L1 12 Z" fill="#444"/></svg>
      <div class="track"><div class="track-fill"></div><div class="knob"></div></div>
      <span class="time">3.47 / 9.29</span>
      <svg class="abs" style="left:306px;top:7px" width="14" height="12" viewBox="0 0 14 12"><path d="M0 4 H4 L8 0 V12 L4 8 H0 Z" fill="#444"/><path d="M10 3 Q12 6 10 9" stroke="#444" fill="none"/></svg>
      <div class="vol"></div>
      <svg class="abs" style="left:393px;top:7px" width="11" height="11" viewBox="0 0 11 11"><rect x="1" y="1" width="9" height="9" fill="none" stroke="#444" stroke-width="1.4"/></svg>
    </div>
  </div>

  <div class="abs rule" style="top:582px"></div>
  <h2 class="abs section-title benefits-title">Experience the benefits of Bloom Within</h2>
  <div class="abs benefits-underline"></div>
  <div class="abs carousel">
    <div class="arrow-btn" style="left:17px"><svg width="8" height="8" viewBox="0 0 8 8"><path d="M5.5 1 L2.5 4 L5.5 7" stroke="#6aa82c" stroke-width="1.6" fill="none"/></svg></div>
    <div class="thumb" style="left:96px"><div role="img" aria-label="Photo: motocross rider on a dirt track" style="background:linear-gradient(135deg,#8a6a3e,#4a3520)"></div></div>
    <div class="thumb" style="left:225px"><div role="img" aria-label="Photo: colourful patterned fabrics" style="background:linear-gradient(135deg,#e86a2a,#c42a7a,#3a9ab0)"></div></div>
    <div class="thumb" style="left:354px"><div role="img" aria-label="Photo: galaxy cluster in deep space" style="background:radial-gradient(circle at 45% 45%,#6a5030,#0a0808 70%)"></div></div>
    <div class="thumb" style="left:483px"><div role="img" aria-label="Photo: icy sea and snowy mountains" style="background:linear-gradient(#7890a8,#c8d4de 45%,#e8eef2)"></div></div>
    <div class="arrow-btn" style="right:17px"><svg width="8" height="8" viewBox="0 0 8 8"><path d="M2.5 1 L5.5 4 L2.5 7" stroke="#6aa82c" stroke-width="1.6" fill="none"/></svg></div>
  </div>

  <div class="abs rule" style="top:774px"></div>
  <h2 class="abs section-title features-title">Features &amp; Benefits</h2>
  <p class="abs features-copy">Sed ut perspiciatis unde omnis iste natus error sit voluptatem accusantium totam rem aperiam, eaque ipsa quae ab illo inventore veritatis et quasi dicta sunt explicabo. Nemo enim ipsam voluptatem quia voluptas sit sed quia consequuntur magni dolores eos qui ratione voluptatem sequi <a href="#">Learn more..</a></p>

  <h2 class="abs section-title students-title">What students are saying?</h2>
  <article class="abs testimonial">
    <div class="avatar" role="img" aria-label="Student portrait"></div>
    <div class="t-title">WONDERFUL PRODUCT FOR STUDENTS</div>
    <div class="t-meta">Posted by <b>Jordan</b> on <b>February 2nd, 2011</b></div>
    <p class="t-body">One of the greatest things I’ve learned about myself is that I really enjoy people. Not only getting to meet people, but getting to connect people also.</p>
    <div class="t-more">Continue Reading “Wonderful Product”</div>
    <div class="t-arrow">→</div>
  </article>

  <div class="abs footer-line"></div>
  <footer class="abs footer">
    <div class="f-head" style="left:20px">QUICK LINKS</div>
    <ul class="quick"><li>HOME</li><li>PRODUCT</li><li>PARENTS</li><li>HOW IT WORKS</li><li>ABOUT US</li><li>CONTACT US</li></ul>

    <div class="f-head" style="left:242px">STAY CONNECTED</div>
    <div class="stay-sub">Follow us for the latest updates and deals</div>
    <ul class="stay-list">
      <li><span style="background:#3b5a9a"></span>Like us on Circlely</li>
      <li><span style="background:#c9302c"></span>Watch us on Vidstream</li>
      <li><span style="background:#3ab5ea"></span>Follow us on Chirper</li>
      <li><span style="background:#f4f4f4"></span>View our Snapfolio photos</li>
    </ul>

    <div class="contact">
      <div style="font-size:11px;font-weight:bold;margin-bottom:6px">CONTACT US</div>
      <div>Call us at +555 010 246</div>
      <div>Fill out our contact form</div>
      <div class="muted" style="margin-top:4px">Copyright 2013. All rights<br>reserved</div>
      <div class="muted" style="margin-top:8px">Terms &amp; Conditions<br>Privacy &nbsp;|&nbsp; Disclaimer</div>
    </div>
    <div class="back-top">Back to Top <span></span></div>
  </footer>
</div>
</body>
</html>
```